Mesh Banner Design for Business Premises

We require the design of a large mesh banner to be installed across the front fence of our warehouse. The banner should prominently feature our existing Trelborn logo and brand colours (yellow, white, and black) and be designed to be highly visible from the road.

The overall aesthetic should be strong, masculine, and industrial, reflecting the nature of the scaffolding and construction industry. The background should be predominantly black, with our branding incorporated in yellow and white for strong contrast and readability.

The banner should clearly communicate the full scope of services we provide, including:

Scaffold Design
Scaffold Engineering
Scaffold Installation / Erection
Scaffold Dismantling

It should also indicate the types of projects and clients we service, including:

Commercial
Industrial
Residential
Civil

The design should feel bold and professional, with a construction-oriented style that aligns with the scaffolding industry. It should be clean, impactful, and easy to read from a distance, ensuring passing traffic can quickly understand our services.

Where possible, subtle industrial or structural design elements (such as scaffold components, steel textures, or linework) may be incorporated into the background to reinforce the industry theme while keeping the layout uncluttered.

The final design will be produced as a large-format mesh banner for outdoor installation, so it should be created with this application and viewing distance in mind.

```html
<!DOCTYPE html>
<html lang="en">
<head>
<meta charset="utf-8">
<title>Trelborn Mesh Banner</title>
<link href="https://fonts.googleapis.com/css2?family=Saira+Condensed:wght@600;700&display=swap" rel="stylesheet">
<style>
  :root {
    --yellow: #f9b21d;
    --black: #0b0b0b;
    --panel: #1d1d1d;
    --white: #ffffff;
    --page: #e9e9e9;
  }
  html, body { margin: 0; padding: 0; overflow: hidden; }
  body {
    width: 848px; height: 1200px;
    background: var(--page);
    font-family: "Saira Condensed", "Arial Narrow", sans-serif;
  }
  .banner {
    position: absolute; left: 0; top: 524px;
    width: 848px; height: 152px;
    background: var(--panel);
    overflow: hidden;
  }
  .structure-texture {
    position: absolute; inset: 0;
    background: linear-gradient(120deg, #262626 0%, #1a1a1a 45%, #2a2a2a 100%);
  }
  .shapes { position: absolute; inset: 0; }
  .brand-name {
    position: absolute; left: 0; width: 264px; top: 64px;
    text-align: center; color: var(--white);
    font-weight: 600; font-size: 17px; letter-spacing: 7px;
  }
  .band-title {
    position: absolute; margin: 0;
    color: var(--black); font-weight: 700; font-size: 15px;
    line-height: 1; letter-spacing: 0.3px;
  }
  .scope-title { left: 289px; top: 48px; }
  .sectors-title { left: 565px; top: 71px; }
  .service-list {
    position: absolute; left: 290px; top: 70px;
    margin: 0; padding: 0; list-style: none;
  }
  .service-list li {
    display: flex; align-items: center; gap: 7px;
    height: 17px; color: var(--white);
    font-weight: 600; font-size: 13px; letter-spacing: 0.3px;
  }
  .service-list svg { width: 16px; height: 14px; flex: none; }
  .sector-tile {
    position: absolute; top: 92px; width: 60px; height: 45px;
    background: var(--yellow); border-radius: 3px;
    box-sizing: border-box; border: 1.5px solid var(--yellow);
  }
  .sector-tile svg { position: absolute; left: 19px; top: 4px; width: 22px; height: 22px; }
  .sector-label {
    position: absolute; left: 1px; right: 1px; bottom: 1px; height: 13px;
    background: var(--black); color: var(--white);
    font-size: 8.5px; font-weight: 600; text-align: center; line-height: 13px;
    border-radius: 0 0 2px 2px;
  }
</style>
</head>
<body>
  <section class="banner">
    <div class="structure-texture" role="img" aria-label="Faint scaffold frame linework across the dark background"></div>
    <svg class="shapes" viewBox="0 0 848 152" width="848" height="152">
      <polygon points="0,0 290,0 256,100 0,100" fill="var(--black)"/>
      <polyline points="0,100 254,100 274,48" fill="none" stroke="var(--yellow)" stroke-width="2"/>
      <polygon points="281,45 573,45 564,64 272,64 " fill="var(--yellow)"/>
      <polygon points="564,68 848,68 848,87 556,87" fill="var(--yellow)"/>
    </svg>

    <div class="brand-name">TRELBORN</div>

    <h2 class="band-title scope-title">SCOPE OF SERVICES</h2>
    <ul class="service-list">
      <li><svg viewBox="0 0 16 14"><rect x="1" y="2" width="13" height="11" fill="none" stroke="#f9b21d"/><path d="M4 5h7M4 8h5M4 11h7" stroke="#f9b21d"/></svg>SCAFFOLD DESIGN</li>
      <li><svg viewBox="0 0 16 14"><circle cx="6" cy="8" r="4" fill="none" stroke="#f9b21d" stroke-width="1.5"/><circle cx="12" cy="4" r="2.5" fill="none" stroke="#f9b21d"/></svg>SCAFFOLD ENGINEERING</li>
      <li><svg viewBox="0 0 16 14"><path d="M3 1v13M13 1v13M3 2h10M3 7h10M3 13h10M3 2l10 5M13 7l-10 6" fill="none" stroke="#f9b21d"/></svg>SCAFFOLD INSTALLATION / ERECTION</li>
      <li><svg viewBox="0 0 16 14"><path d="M1 5h8M1 9h8M11 2l4 10M15 2l-4 10" fill="none" stroke="#f9b21d" stroke-width="1.3"/></svg>SCAFFOLD DISMANTLING</li>
    </ul>

    <h2 class="band-title sectors-title">SECTORS WE SERVICE</h2>
    <div class="sector-tile" style="left:556px">
      <svg viewBox="0 0 22 22"><rect x="5" y="2" width="12" height="19" fill="#0b0b0b"/><path d="M7 5h2M11 5h2M7 9h2M11 9h2M7 13h2M11 13h2" stroke="#f9b21d"/></svg>
      <div class="sector-label">COMMERCIAL</div>
    </div>
    <div class="sector-tile" style="left:628px">
      <svg viewBox="0 0 22 22"><path d="M2 21V12l5-3v3l5-3v3l5-3V3h3v18z" fill="#0b0b0b"/></svg>
      <div class="sector-label">INDUSTRIAL</div>
    </div>
    <div class="sector-tile" style="left:700px">
      <svg viewBox="0 0 22 22"><path d="M11 2L1 11h3v10h5v-6h4v6h5V11h3z" fill="#0b0b0b"/></svg>
      <div class="sector-label">RESIDENTIAL</div>
    </div>
    <div class="sector-tile" style="left:771px">
      <svg viewBox="0 0 22 22"><path d="M9 6h4l3 15H6z" fill="#0b0b0b"/><path d="M11 8v3M11 14v3" stroke="#f9b21d"/><path d="M3 3h16" stroke="#0b0b0b" stroke-width="1.5"/></svg>
      <div class="sector-label">CIVIL</div>
    </div>
  </section>
</body>
</html>
```